Investment website design - investing in mutual funds

I need a design of a website (only homepage for now) dedicated to investment in mutual funds. Attached is a mock up with all the elements the homepage design should contain. The homepage should contain a logo in the upper left corner, the domain the website will run on is www.morvatelsko.cz , in the upper right corner there should be 2 buttons or links SIGN UP / SIGN IN. The bottom of the homepage should contain links to ABOUT US, FAQ, PRIVACY POLICY, CONTACT US.
Now the main elements on the homepage
1) Video that will explain how the investment works exactly, under this video we will have 3 illustrated icons like the ones attached (see 2nd attachement) that will show the potential investor what exactly they could get when investing with us (education for kids, happy life after they retire, regular monthly payment for the rest of their life).
2) On the right side next to the video we will have a calculator where a potential investor can play with the numbers, the investor can fill in the MONTHLY PAYMENT that he wants to invest regularly every month, the time frame of the investment - for how long he wants to invest. Once the potential investor selects those 2 variables we will calculate for him 2 options - either he can get a ONE TIME PAYOUT once he reaches his investment horizon or he can get a regular monthly payment for the rest of his life. Under the laculator there will be a button 'I want to invest ->'. The functionality of the calculator should be similar to the calculator that can be found here http://www.brovikbanka.cz/brovik-podilove-fondy/ and https://pelvaro.cz/.
The design should look similar to https://pelvaro.cz/ (font, colors, logo). We prefer white background in the area where we have the video and calculator. We also like the design of www.truvanex.com. Let me know if you have any questions.

```html
<!DOCTYPE html>
<html lang="en">
<head>
<meta charset="utf-8">
<title>Mutual Funds Investment – Home</title>
<link rel="stylesheet" href="https://fonts.googleapis.com/css2?family=Signika:wght@300;400;600&display=swap">
<style>
  :root {
    --teal-top: #3ea6a0;
    --green-bottom: #63c996;
    --white: #ffffff;
    --line: rgba(255,255,255,0.35);
    --field-text: #6b6f73;
    --accent: #22c9a0;
    --orange-top: #fb8a17;
    --orange-bottom: #ec5530;
    --footer-band: rgba(72,170,140,0.55);
    --video-dark: #1c1c1c;
  }
  * { box-sizing: border-box; margin: 0; padding: 0; }
  html, body { width: 1200px; height: 713px; overflow: hidden; }
  body {
    font-family: "Signika", sans-serif;
    color: var(--white);
    position: relative;
  }
  .hero-backdrop {
    position: absolute; inset: 0;
    background:
      radial-gradient(ellipse 260px 420px at 560px 330px, rgba(90,150,150,0.35), transparent 70%),
      radial-gradient(ellipse 220px 420px at 760px 330px, rgba(120,170,150,0.3), transparent 70%),
      linear-gradient(160deg, var(--teal-top) 0%, #49b59a 55%, var(--green-bottom) 100%);
  }
  .site-header {
    position: absolute; left: 0; top: 0; width: 1200px; height: 77px;
    border-bottom: 1px solid var(--line);
  }
  .brand {
    position: absolute; left: 171px; top: 23px;
    font-size: 21px; font-weight: 600; letter-spacing: 0.2px;
  }
  .auth-btn {
    position: absolute; top: 22px; height: 32px; width: 95px;
    border-radius: 16px; font-size: 14px; font-weight: 300;
    display: flex; align-items: center; justify-content: center; gap: 5px;
    text-decoration: none;
  }
  .auth-btn svg { width: 12px; height: 12px; }
  .auth-btn--signin { left: 830px; background: linear-gradient(#ffffff, #e4e8e8); color: #3aa59e; }
  .auth-btn--signup { left: 933px; border: 1.5px solid var(--white); color: var(--white); }

  .section-title {
    position: absolute; top: 143px;
    font-size: 27px; font-weight: 300;
    display: flex; align-items: center; gap: 15px;
  }
  .section-title svg { width: 25px; height: 25px; }
  .section-title--video { left: 172px; }
  .section-title--calc { left: 641px; }

  .video-frame {
    position: absolute; left: 172px; top: 198px; width: 392px; height: 255px;
    background: radial-gradient(ellipse at 40% 45%, #3a3a3a, var(--video-dark) 75%);
  }
  .play-button { position: absolute; left: 164px; top: 95px; width: 66px; height: 66px; }

  .benefit {
    position: absolute; top: 465px; width: 123px; height: 137px;
    border: 1px dashed rgba(255,255,255,0.55);
    text-align: center;
  }
  .benefit__art {
    width: 80px; height: 52px; margin: 14px auto 0;
    border-radius: 10px;
    background: linear-gradient(135deg, #f6a623, #e8553a);
    opacity: 0.85;
  }
  .benefit__label {
    position: absolute; left: 0; right: 0; top: 92px;
    font-size: 14.5px; font-weight: 300; line-height: 17px;
  }
  .benefit--kids { left: 172px; }
  .benefit--income { left: 306px; }
  .benefit--retire { left: 441px; }

  .column-divider {
    position: absolute; left: 599px; top: 152px; width: 1px; height: 450px;
    background: var(--line);
  }

  .field {
    position: absolute; left: 637px; width: 390px; height: 40px;
    background: var(--white); border-radius: 2px;
    box-shadow: 0 2px 0 rgba(0,0,0,0.12);
    color: var(--field-text); font-size: 11.5px; font-weight: 300;
    padding-left: 14px; display: flex; align-items: center;
  }
  .field--monthly { top: 198px; }
  .field--payout { top: 329px; }
  .field--pension { top: 419px; }

  .slider-label {
    position: absolute; left: 636px; top: 250px;
    font-size: 14px; font-weight: 600;
  }
  .slider-track {
    position: absolute; left: 637px; top: 283px; width: 390px; height: 10px;
    border-radius: 5px; background: var(--white);
  }
  .slider-fill {
    position: absolute; left: 0; top: 0; width: 72px; height: 10px; border-radius: 5px 0 0 5px;
    background: repeating-linear-gradient(45deg, var(--accent) 0 2px, #5fe0bd 2px 4px);
  }
  .slider-thumb {
    position: absolute; left: 699px; top: 278px; width: 21px; height: 21px; border-radius: 50%;
    background: var(--white); box-shadow: 0 1px 3px rgba(0,0,0,0.25);
  }
  .slider-thumb::after {
    content: ""; position: absolute; left: 8px; top: 8px; width: 5px; height: 5px;
    border-radius: 50%; background: var(--accent);
  }
  .slider-scale {
    position: absolute; top: 303px; font-size: 11px; font-weight: 300;
  }
  .slider-scale--min { left: 637px; }
  .slider-scale--max { left: 983px; }

  .or-divider {
    position: absolute; left: 637px; top: 394px; width: 390px; height: 1px; background: var(--line);
  }
  .or-divider span {
    position: absolute; left: 182px; top: -13px; width: 26px; height: 26px; border-radius: 50%;
    border: 1px solid var(--line); background: rgba(80,175,150,0.9);
    font-size: 10px; display: flex; align-items: center; justify-content: center;
  }

  .invest-btn {
    position: absolute; left: 637px; top: 483px; width: 390px; height: 41px;
    border-radius: 3px; background: linear-gradient(var(--orange-top), var(--orange-bottom));
    box-shadow: 0 2px 0 rgba(150,50,20,0.35);
    font-size: 15.5px; font-weight: 600; letter-spacing: 0.2px;
    display: flex; align-items: center; justify-content: center;
  }

  .site-footer {
    position: absolute; left: 0; top: 678px; width: 1200px; height: 35px;
    background: var(--footer-band);
    display: flex; align-items: center; justify-content: center;
    font-size: 10.5px; font-weight: 300; gap: 7px;
  }
</style>
</head>
<body>
  <div class="hero-backdrop" role="img" aria-label="Photo of an older couple walking hand in hand on a beach, tinted teal-green"></div>

  <header class="site-header">
    <div class="brand">Company Logo</div>
    <a class="auth-btn auth-btn--signin" href="#">
      <svg viewBox="0 0 12 12" fill="none" stroke="currentColor" stroke-width="1.2"><path d="M5 1h6v10H5M1 6h6M5 4l2 2-2 2"/></svg>Sign In
    </a>
    <a class="auth-btn auth-btn--signup" href="#">
      <svg viewBox="0 0 12 12" fill="none" stroke="currentColor" stroke-width="1.2"><path d="M9 1.5H1v9.5h9.5V6M5 7l6-6"/></svg>Sign Up
    </a>
  </header>

  <h2 class="section-title section-title--video">
    <svg viewBox="0 0 25 25" fill="none" stroke="#fff" stroke-width="1.2"><rect x="1" y="1" width="23" height="23"/><path d="M1 17h23M10 5l5 3-5 3z M4 21h2 M9 21h12"/></svg>
    Video About Our Product
  </h2>
  <div class="video-frame" role="img" aria-label="Video still: hand writing a dollar sign next to the words Mutual Funds">
    <svg class="play-button" viewBox="0 0 66 66"><circle cx="33" cy="33" r="30" fill="none" stroke="#fff" stroke-width="5"/><path d="M27 21l18 12-18 12z" fill="#fff"/></svg>
  </div>

  <div class="benefit benefit--kids">
    <div class="benefit__art" role="img" aria-label="Illustration of stacked books with a graduation cap"></div>
    <div class="benefit__label">Education<br>for Kids</div>
  </div>
  <div class="benefit benefit--income">
    <div class="benefit__art" role="img" aria-label="Illustration of a cuckoo clock dropping coins"></div>
    <div class="benefit__label">Passive<br>Income</div>
  </div>
  <div class="benefit benefit--retire">
    <div class="benefit__art" role="img" aria-label="Illustration of a person relaxing in a hammock"></div>
    <div class="benefit__label">Happy<br>Retirement</div>
  </div>

  <div class="column-divider"></div>

  <h2 class="section-title section-title--calc">
    <svg viewBox="0 0 25 25" fill="none" stroke="#fff" stroke-width="1.2"><rect x="1" y="2" width="23" height="16"/><rect x="3" y="4" width="19" height="12"/><path d="M12.5 18v4M8 23h9"/></svg>
    Our Online Calculator
  </h2>
  <div class="field field--monthly">Regular monthly investment:</div>
  <div class="slider-label">Length of investment</div>
  <div class="slider-track"><div class="slider-fill"></div></div>
  <div class="slider-thumb"></div>
  <div class="slider-scale slider-scale--min">0</div>
  <div class="slider-scale slider-scale--max">30 Years</div>
  <div class="field field--payout">One time payout:</div>
  <div class="or-divider"><span>OR</span></div>
  <div class="field field--pension">Mothly payment:</div>
  <div class="invest-btn">I WANT TO INVEST</div>

  <footer class="site-footer">
    <span>ABOUT US</span><span>|</span><span>FAQ</span><span>|</span><span>PRIVACY POLICY</span><span>|</span><span>CONTACT</span>
  </footer>
</body>
</html>
```